Torvel Cleaning Company Flyer

Hi, We need an A4 flyer design for our cleaning company, focusing on dry carpet cleaning I attached our catalogue to give some idea. In addition, our websites can provide more information. Our Services:-General Cleaning Carry out heavy cleansing tasks and special projects. Clean, stock and supply designated facility areas (dusting, sweeping, vacuuming, mopping, cleaning ceiling vents, restroom cleaning etc).Using electrically powered scrubbing and polishing machines to burnish, scrub, polish and spray clean floors. Window Cleaning Regular, Reliable Window Cleaning.Hard To Reach Windows.Single 7 Multi-Storey.Frames and Glass Cleaned.Floor Cleaning Cleaning Marble Cleaning & Polishing.Tile & Grout Cleaning.Hardwood Floors Services.Vinyl Floors.The MIRA Dry Extraction Carpet Cleaning System uses environmentally preferred, Blue Fern Certified cleaning products that deep cleans your carpets and textured hard floors quickly and easily.

Target Market(s)

Commercial Cleaning residential Cleaning Hotel cleaning

Industry/Entity Type

Cleaning Service

Contact Information for Business Card

Samir Tareq Al-Hudhaili Gm
Derek Plume Marketing Manger

Font styles to use
Serif
Sans Serif

Colors
0355a3
3176b5
85acd3
cee9f5
85cae6
34a6d7
0592cd

```html
<!DOCTYPE html>
<html lang="en">
<head>
<meta charset="utf-8">
<title>Torvel Cleaning Company Flyer</title>
<link href="https://fonts.googleapis.com/css2?family=Lato:wght@400;700;900&family=Montserrat:wght@300;400;700;800&display=swap" rel="stylesheet">
<style>
  :root {
    --navy: #0355a3;
    --mid-blue: #3176b5;
    --soft-blue: #85acd3;
    --ice: #cee9f5;
    --sky: #85cae6;
    --bright: #34a6d7;
    --cyan: #0592cd;
    --headline: #1f6fe0;
    --ink: #1a2230;
    --backdrop: #1b1b1b;
    --ribbon: #0a0a0a;
  }
  * { margin: 0; padding: 0; box-sizing: border-box; }
  html, body { width: 1200px; height: 1200px; overflow: hidden; background: var(--backdrop); }
  .flyer-wrap { position: absolute; left: 273px; top: 137px; width: 663px; height: 937px; overflow: hidden; }
  .flyer { position: absolute; left: 0; top: 0; width: 829px; height: 1172px; transform: scale(0.8); transform-origin: 0 0; background: #fff; font-family: 'Lato', sans-serif; overflow: hidden; }
  .hero-photo { position: absolute; left: 0; top: 0; width: 600px; height: 640px;
    background: linear-gradient(90deg, rgba(255,255,255,0) 70%, #fff 100%), linear-gradient(180deg, #dfe3e6 0%, #eef0f1 30%, #f6f6f6 55%, #e4dcd4 100%); }
  .waves { position: absolute; left: 0; top: 0; width: 829px; height: 1172px; }
  .brand { position: absolute; left: 560px; top: 58px; width: 260px; display: flex; align-items: center; gap: 10px; justify-content: center; }
  .brand-mark { width: 22px; height: 22px; border-radius: 50%; background: var(--cyan); flex: none; }
  .brand-name { font-family: 'Montserrat', sans-serif; font-weight: 700; font-size: 26px; line-height: 1.05; color: var(--navy); }
  .title-pro { position: absolute; left: 592px; top: 142px; font-family: 'Montserrat', sans-serif; font-weight: 700; font-size: 24px; color: var(--ink); }
  .title-main { position: absolute; left: 574px; top: 170px; font-family: 'Montserrat', sans-serif; font-weight: 800; font-size: 50px; color: var(--headline); line-height: 1; }
  .title-sub { position: absolute; left: 592px; top: 222px; font-family: 'Montserrat', sans-serif; font-weight: 400; font-size: 38px; color: var(--mid-blue); line-height: 1; }
  .tab { position: absolute; background: var(--navy); color: #fff; font-family: 'Montserrat', sans-serif; font-weight: 700; display: flex; align-items: center; }
  .tab-services { left: 541px; top: 277px; width: 288px; height: 46px; border-radius: 23px 0 0 23px; padding-left: 34px; font-size: 31px; }
  .tab-about { left: 0; top: 703px; width: 238px; height: 46px; border-radius: 0 23px 23px 0; padding-left: 36px; font-size: 32px; }
  .service-list { position: absolute; left: 578px; top: 328px; list-style: none; }
  .service-list li { font-size: 19px; font-weight: 700; color: var(--ink); height: 33.5px; line-height: 33.5px; padding-left: 19px; position: relative; }
  .service-list li::before { content: ""; position: absolute; left: 0; top: 13px; width: 9px; height: 9px; border-radius: 50%; background: var(--ink); }
  .about-text { position: absolute; left: 22px; top: 761px; width: 310px; font-size: 14.6px; font-weight: 700; line-height: 18.5px; color: var(--ink); letter-spacing: -0.2px; }
  .contact { position: absolute; left: 0; width: 400px; height: 60px; }
  .contact-web { top: 1008px; }
  .contact-phone { top: 1088px; }
  .contact-bar { position: absolute; left: 48px; top: 7px; height: 46px; width: 350px; background: var(--navy); clip-path: polygon(0 0, 100% 0, 88% 100%, 0 100%); color: #fff; font-weight: 700; display: flex; align-items: center; padding-left: 40px; }
  .contact-web .contact-bar { font-size: 15.5px; }
  .contact-phone .contact-bar { font-size: 18px; padding-left: 52px; }
  .contact-icon { position: absolute; top: 1px; width: 58px; height: 58px; border-radius: 50%; background: #fff; border: 4px solid #000; display: flex; align-items: center; justify-content: center; }
  .contact-web .contact-icon { left: 16px; }
  .contact-phone .contact-icon { left: 24px; }
  .feature { position: absolute; width: 206px; height: 206px; border-radius: 50%; border: 7px solid var(--navy); overflow: hidden; }
  .feature-carpet { left: 330px; top: 690px; background: linear-gradient(135deg, #8a5a3a 0%, #c9b8a8 45%, #2a3550 70%, #e8e4df 100%); }
  .feature-door { left: 596px; top: 636px; background: linear-gradient(135deg, #7a4a2a 0%, #a9734b 50%, #232b3d 80%, #8e5f3d 100%); }
  .feature-window { left: 496px; top: 907px; background: linear-gradient(135deg, #dfe6ea 0%, #f4f2ef 40%, #e9c27a 65%, #4cbfb4 100%); }
  .ribbon { position: absolute; width: 235px; height: 44px; background: var(--ribbon); color: #fff; font-family: 'Lato', sans-serif; font-weight: 700; font-size: 23px; display: flex; align-items: center; justify-content: center; transform: rotate(-20deg); clip-path: polygon(0 0, 100% 0, 96% 50%, 100% 100%, 0 100%, 4% 50%); }
  .ribbon-carpet { left: 333px; top: 851px; }
  .ribbon-door { left: 604px; top: 803px; }
  .ribbon-window { left: 503px; top: 1089px; }
</style>
</head>
<body>
<div class="flyer-wrap">
  <div class="flyer">
    <div class="hero-photo" role="img" aria-label="Photo of a person mopping a bright white kitchen floor"></div>

    <svg class="waves" viewBox="0 0 829 1172" aria-hidden="true">
      <defs>
        <linearGradient id="lowerBlue" x1="0" y1="0" x2="0" y2="1">
          <stop offset="0" stop-color="#a9dcf2"/>
          <stop offset="1" stop-color="#9fd5ee"/>
        </linearGradient>
      </defs>
      <path d="M0,405 C160,385 330,470 480,560 C610,632 730,640 829,610 L829,1172 L0,1172 Z" fill="url(#lowerBlue)"/>
      <path d="M0,402 C160,380 330,462 480,552" fill="none" stroke="#fff" stroke-width="6"/>
      <path d="M0,452 C140,420 320,470 455,598 C330,560 160,575 0,650 Z" fill="var(--navy)"/>
      <path d="M560,575 C690,560 790,520 829,480 L829,575 C760,610 660,605 560,575 Z" fill="var(--bright)"/>
      <path d="M545,590 C680,600 780,575 829,545 L829,605 C740,630 640,625 545,590 Z" fill="var(--navy)"/>
      <path d="M545,600 C680,622 780,612 829,592" fill="none" stroke="#fff" stroke-width="5"/>
    </svg>

    <div class="brand">
      <span class="brand-mark"></span>
      <span class="brand-name">Torvel Cleaning</span>
    </div>

    <div class="title-pro">Professional</div>
    <div class="title-main">Cleaning</div>
    <div class="title-sub">Service</div>

    <div class="tab tab-services">Services</div>
    <ul class="service-list">
      <li>Dusting</li>
      <li>Sweeping</li>
      <li>Vacuuming</li>
      <li>Mopping</li>
      <li>Cleaning ceiling vents</li>
      <li>Restroom cleaning</li>
    </ul>

    <div class="tab tab-about">About Us</div>
    <p class="about-text">With over 24 years in operation, Torvel Cleaning Est. has established itself as a successful business in the cleaning and hospitality industry and has accumulated expert knowledge on cleaning processes and procedures to ensure your premises are maintained to the highest standards. Our staff are chosen meticulously through rigorous interview and employment procedures so that you can feel comfortable leaving your property and assets in safe, secure and professional hands.</p>

    <div class="contact contact-web">
      <div class="contact-bar">torvelcleaning1993.business.site</div>
      <div class="contact-icon">
        <svg width="32" height="32" viewBox="0 0 32 32" aria-hidden="true">
          <circle cx="16" cy="16" r="13" fill="none" stroke="#000" stroke-width="2.5"/>
          <ellipse cx="16" cy="16" rx="6" ry="13" fill="none" stroke="#000" stroke-width="2"/>
          <line x1="3" y1="16" x2="29" y2="16" stroke="#000" stroke-width="2"/>
        </svg>
      </div>
    </div>

    <div class="contact contact-phone">
      <div class="contact-bar">Call Us&nbsp; @&nbsp; 4491 5586</div>
      <div class="contact-icon">
        <svg width="30" height="30" viewBox="0 0 24 24" aria-hidden="true">
          <path d="M6.6 10.8c1.4 2.8 3.8 5.2 6.6 6.6l2.2-2.2c.3-.3.7-.4 1-.2 1.1.4 2.3.6 3.6.6.6 0 1 .4 1 1V20c0 .6-.4 1-1 1C10.6 21 3 13.4 3 4c0-.6.4-1 1-1h3.5c.6 0 1 .4 1 1 0 1.3.2 2.5.6 3.6.1.3 0 .7-.2 1L6.6 10.8z" fill="none" stroke="#000" stroke-width="1.6"/>
        </svg>
      </div>
    </div>

    <div class="feature feature-carpet" role="img" aria-label="Photo of a technician cleaning carpet with a machine"></div>
    <div class="feature feature-door" role="img" aria-label="Photo of a cleaner wiping a wooden door"></div>
    <div class="feature feature-window" role="img" aria-label="Photo of a cleaner washing a window"></div>

    <div class="ribbon ribbon-carpet">Carpet Cleaning</div>
    <div class="ribbon ribbon-door">Door Cleaning</div>
    <div class="ribbon ribbon-window">Window Cleaning</div>
  </div>
</div>
</body>
</html>
```